Ferncrest Dental, LLC business card project

Business card to be designed with current logo.
Dental office- please keep design of card that looks clean and professional.
Please include the following info:
Ferncrest Dental, LLC
Dr. Lorna Pettigrew
2871 Marlowe Street
Bethlehem, PA 18093
610-555-0193
ferncrestdental.office@examplemail.test
Hello everyone-
Reason: Just got back from overseas- will look at all designs and provide feedback. Thank you!
Reason: Polling my friends for the final selection-
thank you to all those that participated- so many talented designers!

```html
<!DOCTYPE html>
<html lang="en">
<head>
<meta charset="utf-8">
<title>Ferncrest Dental, LLC – Business Card</title>
<link href="https://fonts.googleapis.com/css2?family=Questrial&display=swap" rel="stylesheet">
<style>
  :root {
    --stage: #000000;
    --paper: #ffffff;
    --ink: #231f20;
    --leaf: #6aa842;
    --lime: #b8cf42;
    --lime-soft: #d4e28a;
    --mist: #eef4ea;
    --grey-band: #bdbdbd;
  }
  * { margin: 0; padding: 0; box-sizing: border-box; }
  html, body {
    width: 1200px; height: 848px; overflow: hidden;
    background: var(--stage);
    font-family: "Questrial", "Century Gothic", sans-serif;
  }
  .stage { position: relative; width: 1200px; height: 848px; }
  .card {
    position: absolute; left: 379px; width: 442px; height: 270px; overflow: hidden;
  }
  .card--front { top: 129px; background: var(--paper); }
  .card--back { top: 436px; background: var(--lime); }

  .brand {
    position: absolute; left: 22px; top: 24px;
    display: flex; align-items: center; gap: 8px;
  }
  .brand__dot { width: 14px; height: 14px; border-radius: 50%; background: var(--lime); }
  .brand__name { font-size: 24px; color: var(--leaf); letter-spacing: -0.2px; line-height: 1; }

  .scene {
    position: absolute; left: 14px; top: 74px; width: 245px; height: 185px;
    background: linear-gradient(180deg, #ffffff 0%, #f1f1f1 45%, var(--mist) 100%);
    border-radius: 90px 90px 0 0;
  }
  .card--back .scene {
    left: 28px; top: 7px; width: 370px; height: 263px;
    background: linear-gradient(180deg, var(--lime) 0%, #c6d966 55%, var(--lime-soft) 100%);
    border-radius: 140px 140px 0 0;
  }

  .contact {
    position: absolute; right: 25px; top: 187px;
    text-align: right; color: var(--ink);
  }
  .contact__name {
    position: absolute; right: 25px; top: 152px;
    font-size: 14.5px; font-weight: 700; color: var(--leaf);
    white-space: nowrap;
  }
  .contact__line { font-size: 11.6px; line-height: 14.5px; white-space: nowrap; }

  .bands { position: absolute; left: 0; bottom: 0; width: 100%; height: 10px; }
  .band { position: absolute; top: 0; height: 10px; }
  .band--grey { left: 0; width: 335px; background: var(--grey-band); }
  .band--lime { left: 341px; width: 66px; background: var(--lime); }
  .band--leaf { left: 413px; width: 29px; background: var(--leaf); }
</style>
</head>
<body>
<main class="stage">
  <section class="card card--front" aria-label="Card front">
    <div class="brand">
      <span class="brand__dot"></span>
      <span class="brand__name">Ferncrest Dental</span>
    </div>
    <div class="scene" role="img" aria-label="Soft illustration of a large tooth beside two trees on a gentle hill"></div>
    <p class="contact__name">Dr. Lorna Pettigrew</p>
    <address class="contact" style="font-style:normal">
      <p class="contact__line">Ferncrest Dental, LLC</p>
      <p class="contact__line">2871 Marlowe Street Bethlehem,</p>
      <p class="contact__line">PA 18093 610-555-0193</p>
      <p class="contact__line">ferncrestdental.office@examplemail.test</p>
    </address>
    <div class="bands">
      <span class="band band--grey"></span>
      <span class="band band--lime"></span>
      <span class="band band--leaf"></span>
    </div>
  </section>

  <section class="card card--back" aria-label="Card back">
    <div class="scene" role="img" aria-label="Light green outline of a tooth with two trees on a hill"></div>
  </section>
</main>
</body>
</html>
```